80s Dance Party invitation/flyer

Im looking for a flyer for an 80’s theme party called Radically Groovy 80’s Dance Party. Date is Saturday, June 26, 2021. Location: Marlowe Commons. Uploaded are some sample ideas i like.

```html
<!DOCTYPE html>
<html lang="en">
<head>
<meta charset="UTF-8">
<title>Radically Groovy 80’s Dance Party</title>
<link rel="stylesheet" href="https://fonts.googleapis.com/css2?family=Audiowide&family=Bungee+Inline&family=Permanent+Marker&family=Quicksand:wght@700&family=Righteous&display=block">
<style>
  :root {
    --night: #1c0f3f;
    --violet: #4a1d86;
    --magenta: #c2267a;
    --sunset: #f08a3a;
    --gold: #f6e27a;
    --chrome-top: #8ff3e8;
    --chrome-mid: #2a9fb6;
    --chrome-low: #f07aa8;
    --chrome-base: #ffe7a0;
    --neon-green: #2fd14e;
    --party-pink: #e0326f;
    --ink: #241a3d;
    --cream: #f3ecd6;
    --deck-blue: #2f8fd0;
    --box-blue: #3b5fb5;
    --tape-pink: #e24fa3;
  }
  html, body {
    margin: 0;
    padding: 0;
    width: 956px;
    height: 1200px;
    overflow: hidden;
    background: var(--night);
  }
  .flyer {
    position: relative;
    width: 956px;
    height: 1200px;
    overflow: hidden;
    background:
      radial-gradient(ellipse 60% 40% at 50% 30%, rgba(120, 80, 230, 0.55), transparent 70%),
      linear-gradient(180deg, #2b154f 0%, var(--violet) 35%, #6a1f87 55%, var(--magenta) 72%, var(--sunset) 88%, var(--gold) 100%);
  }
  .spotlights {
    position: absolute;
    inset: 0;
  }
  .art-sunset {
    position: absolute;
    left: 263px;
    top: 785px;
    width: 430px;
    height: 430px;
    border-radius: 50%;
    background: radial-gradient(circle at 50% 60%, rgba(255, 242, 168, 0.85), rgba(245, 192, 122, 0.55) 70%, rgba(245, 192, 122, 0) 100%);
  }
  .headline-small {
    position: absolute;
    left: 42px;
    font-family: "Righteous", sans-serif;
    font-size: 66px;
    line-height: 1;
    letter-spacing: 1px;
    background: linear-gradient(180deg, var(--chrome-top) 0%, var(--chrome-mid) 48%, var(--chrome-low) 52%, var(--chrome-base) 100%);
    -webkit-background-clip: text;
    background-clip: text;
    color: transparent;
    -webkit-text-stroke: 1.5px #2a2140;
  }
  .headline-small.first { top: 138px; }
  .headline-small.second { top: 218px; left: 92px; }
  .headline-decade {
    position: absolute;
    left: 470px;
    top: 86px;
    font-family: "Righteous", sans-serif;
    font-size: 190px;
    line-height: 1;
    background: linear-gradient(180deg, var(--chrome-top) 0%, var(--chrome-mid) 46%, var(--chrome-low) 54%, var(--chrome-base) 100%);
    -webkit-background-clip: text;
    background-clip: text;
    color: transparent;
    -webkit-text-stroke: 3px var(--cream);
  }
  .headline-dance {
    position: absolute;
    left: 0;
    width: 956px;
    top: 296px;
    text-align: center;
    font-family: "Bungee Inline", sans-serif;
    font-size: 84px;
    line-height: 1;
    color: var(--neon-green);
    text-shadow: 4px 4px 0 #0c3a1a;
  }
  .headline-party {
    position: absolute;
    left: 0;
    width: 956px;
    top: 384px;
    text-align: center;
    font-family: "Permanent Marker", cursive;
    font-size: 124px;
    line-height: 1;
    color: var(--party-pink);
    text-shadow: 4px 4px 0 #4a0f2a;
  }
  .art-boombox {
    position: absolute;
    left: 64px; top: 572px;
    width: 270px; height: 272px;
    border-radius: 14px;
    background: linear-gradient(160deg, #5f7fd6, var(--box-blue) 60%, #23306e);
  }
  .art-cassette {
    position: absolute;
    left: 640px; top: 602px;
    width: 276px; height: 200px;
    border-radius: 12px;
    background: linear-gradient(160deg, #f27cc0, var(--tape-pink) 55%, #a3256f);
  }
  .art-turntable {
    position: absolute;
    left: 302px; top: 540px;
    width: 358px; height: 326px;
    border-radius: 36px;
    background: radial-gradient(circle at 58% 55%, #2a2236 0 34%, var(--deck-blue) 35% 100%);
    box-shadow: 0 8px 18px rgba(0,0,0,0.35);
  }
  .date-band {
    position: absolute;
    left: 137px;
    top: 880px;
    width: 718px;
    height: 50px;
    border-top: 5px solid var(--cream);
    border-bottom: 5px solid var(--cream);
    text-align: center;
    font-family: "Audiowide", sans-serif;
    font-size: 39px;
    line-height: 50px;
    letter-spacing: 1px;
    color: var(--cream);
    text-shadow: 2px 2px 0 #3a2a50;
  }
  .location {
    position: absolute;
    left: 0;
    width: 956px;
    top: 956px;
    text-align: center;
    font-family: "Quicksand", sans-serif;
    font-weight: 700;
    font-size: 40px;
    color: var(--ink);
  }
</style>
</head>
<body>
  <main class="flyer">
    <svg class="spotlights" width="956" height="1200" viewBox="0 0 956 1200" aria-hidden="true">
      <defs>
        <linearGradient id="beam" x1="0" y1="0" x2="0" y2="1">
          <stop offset="0" stop-color="#ff5fb0" stop-opacity="0.55"/>
          <stop offset="1" stop-color="#ff5fb0" stop-opacity="0"/>
        </linearGradient>
        <linearGradient id="beam-violet" x1="0" y1="0" x2="0" y2="1">
          <stop offset="0" stop-color="#b58bff" stop-opacity="0.5"/>
          <stop offset="1" stop-color="#b58bff" stop-opacity="0"/>
        </linearGradient>
      </defs>
      <polygon points="60,0 200,0 420,560 300,560" fill="url(#beam)"/>
      <polygon points="760,0 900,0 640,560 520,560" fill="url(#beam)"/>
      <polygon points="0,420 60,400 140,900 0,920" fill="url(#beam-violet)"/>
      <polygon points="896,380 956,360 956,920 820,880" fill="url(#beam-violet)"/>
      <g stroke="#8a7ae0" stroke-opacity="0.25" stroke-width="1.5">
        <line x1="200" y1="150" x2="760" y2="150"/>
        <line x1="200" y1="280" x2="760" y2="280"/>
        <line x1="200" y1="410" x2="760" y2="410"/>
        <line x1="200" y1="540" x2="760" y2="540"/>
        <line x1="260" y1="100" x2="260" y2="560"/>
        <line x1="400" y1="100" x2="400" y2="560"/>
        <line x1="540" y1="100" x2="540" y2="560"/>
        <line x1="680" y1="100" x2="680" y2="560"/>
      </g>
      <circle cx="190" cy="80" r="30" fill="#5ad19a" opacity="0.25"/>
      <circle cx="870" cy="50" r="24" fill="#ff6fa8" opacity="0.35"/>
      <circle cx="920" cy="635" r="28" fill="#6ad08a" opacity="0.35"/>
      <circle cx="200" cy="1110" r="28" fill="#6a8a40" opacity="0.4"/>
      <circle cx="80" cy="330" r="60" fill="#7a50c0" opacity="0.2"/>
    </svg>

    <div class="art-sunset" role="img" aria-label="Retro striped sunset illustration"></div>

    <div class="headline-small first">RADICALLY</div>
    <div class="headline-small second">GROOVY</div>
    <div class="headline-decade">80’s</div>
    <div class="headline-dance">DANCE</div>
    <div class="headline-party">PARTY</div>

    <div class="art-boombox" role="img" aria-label="Illustration of a retro boombox"></div>
    <div class="art-cassette" role="img" aria-label="Illustration of a pink cassette tape"></div>
    <div class="art-turntable" role="img" aria-label="Illustration of a record turntable icon"></div>

    <div class="date-band">SATURDAY, JUNE 26, 2021</div>
    <div class="location">Location: Marlowe Commons</div>
  </main>
</body>
</html>
```